Label for ORGANIC ROSE WATER

Organic Rose Water is a second product from a family of products that we develop. The first product was Organic Argan Oil. The label for this product should be in the same style as the first label that we have. The bottle will be exactly the same. It is good to know that the text should be in GOLD colour (not yellow) it is possible that we continue the same gold or use ROSE (pink) gold. We still have not decided what will suit more.
The fonts that are used in this labels are:
Raleway
and
Butler
both fonts can be found in typemeadow for free
Women and girls.
Cosmetics
- Black label, gold or pink gold colours.
- As this is rose water and the label is minimalistic, the designer should find the best way to input somewhere and somehow rose colour to make the product recognisable.

```html
<!DOCTYPE html>
<html lang="en">
<head>
<meta charset="utf-8">
<title>Organic Rose Water Label</title>
<link href="https://fonts.googleapis.com/css2?family=Raleway:wght@400;500&family=Playfair+Display:wght@900&display=swap" rel="stylesheet">
<style>
  :root {
    --page: #f4f4f4;
    --label-black: #0d0d0d;
    --gold: #c9a36a;
    --gold-light: #e6c98f;
    --gold-dark: #a17a3e;
    --ink: #111111;
    --rose: #d99a9a;
    --rose-deep: #b86f72;
    --leaf: #8b9a7c;
  }
  html, body {
    margin: 0;
    padding: 0;
    width: 1177px;
    height: 1200px;
    overflow: hidden;
    background: var(--page);
  }
  .canvas {
    position: relative;
    width: 1177px;
    height: 1200px;
  }
  .label {
    position: absolute;
    left: 318px;
    top: 130px;
    width: 540px;
    height: 940px;
    background: linear-gradient(180deg, #161616 0%, var(--label-black) 60%, #080808 100%);
    font-family: "Raleway", sans-serif;
    color: var(--gold);
  }
  .brand-name {
    position: absolute;
    left: 0;
    right: 0;
    top: 200px;
    text-align: center;
    font-family: "Raleway", sans-serif;
    font-weight: 500;
    font-size: 62px;
    letter-spacing: 3px;
    color: var(--gold);
  }
  .rose-art {
    position: absolute;
    left: 300px;
    top: 430px;
    width: 190px;
    height: 170px;
  }
  .product-word {
    position: absolute;
    left: 60px;
    top: 582px;
    font-size: 30px;
    font-weight: 500;
    letter-spacing: 3px;
    color: var(--gold);
  }
  .product-plate {
    position: absolute;
    left: 60px;
    top: 626px;
    width: 330px;
    height: 150px;
    background: linear-gradient(120deg, var(--gold-dark) 0%, var(--gold-light) 45%, var(--gold) 70%, var(--gold-dark) 100%);
  }
  .product-rose {
    position: absolute;
    left: 12px;
    top: -14px;
    font-family: "Playfair Display", serif;
    font-weight: 900;
    font-size: 120px;
    line-height: 1;
    color: var(--ink);
  }
  .product-water {
    position: absolute;
    right: 14px;
    bottom: 8px;
    font-size: 30px;
    font-weight: 500;
    letter-spacing: 1px;
    color: var(--ink);
  }
  .details {
    position: absolute;
    left: 60px;
    top: 812px;
    border-left: 2px solid var(--gold);
    padding-left: 14px;
  }
  .details-main {
    font-size: 21px;
    line-height: 1.3;
    margin: 0 0 14px;
  }
  .details-sub {
    font-size: 14px;
    line-height: 1.4;
    margin: 0;
  }
  .volume {
    position: absolute;
    right: 60px;
    top: 872px;
    text-align: right;
    font-size: 15px;
    line-height: 1.4;
  }
</style>
</head>
<body>
<div class="canvas">
  <section class="label">
    <div class="brand-name">velmora</div>

    <svg class="rose-art" viewBox="0 0 190 170" role="img" aria-label="Illustration of pink roses with green leaves">
      <defs>
        <radialGradient id="roseTone" cx="50%" cy="45%" r="55%">
          <stop offset="0%" stop-color="#e8b4ae"/>
          <stop offset="70%" stop-color="#c98a88"/>
          <stop offset="100%" stop-color="rgba(120,130,100,0.6)"/>
        </radialGradient>
      </defs>
      <ellipse cx="95" cy="85" rx="90" ry="78" fill="url(#roseTone)" opacity="0.85"/>
    </svg>

    <div class="product-word">ORGANIC</div>
    <div class="product-plate">
      <span class="product-rose">rose</span>
      <span class="product-water">WATER</span>
    </div>

    <div class="details">
      <p class="details-main">100% pure and natural<br>Rosa Damascena</p>
      <p class="details-sub">BIO Rosenwasser<br>Eau de Rose BIO</p>
    </div>
    <div class="volume">100ml ℮<br>3.38 fl.oz</div>
  </section>
</div>
</body>
</html>
```